Eid Logo Design/message

I need to design a beautiful logo/design for eid Mubarak-

For the following person-

Oulima( in Arabic and in English)

Message- Eid Mubarak

```html
<!DOCTYPE html>
<html lang="en">
<head>
<meta charset="utf-8">
<title>Eid Mubarak – Oulima</title>
<link rel="stylesheet" href="https://fonts.googleapis.com/css2?family=Great+Vibes&family=Montserrat:wght@400&family=Amiri&family=Allura&display=swap">
<style>
  :root {
    --blue-core: #21618d;
    --blue-mid: #1b5480;
    --blue-edge: #0f3a5e;
    --ink-white: #ffffff;
    --ink-soft: #e4e8ec;
  }
  html, body {
    margin: 0;
    padding: 0;
    overflow: hidden;
    background: var(--blue-edge);
  }
  .greeting-card {
    position: relative;
    width: 937px;
    height: 1200px;
    overflow: hidden;
    background:
      radial-gradient(ellipse 70% 60% at 52% 45%, var(--blue-core) 0%, var(--blue-mid) 55%, var(--blue-edge) 100%);
  }
  .mosque-emblem {
    position: absolute;
    left: 270px;
    top: 270px;
    width: 215px;
    height: 370px;
    border-radius: 90px 90px 6px 6px;
    background: linear-gradient(180deg, rgba(255,255,255,0.9), rgba(255,255,255,0.8));
  }
  .crescent-star {
    position: absolute;
    left: 535px;
    top: 400px;
    width: 115px;
    height: 125px;
  }
  .eid-title {
    position: absolute;
    left: 255px;
    top: 455px;
    margin: 0;
    font-family: "Great Vibes", cursive;
    font-weight: 400;
    font-size: 290px;
    line-height: 1;
    color: var(--ink-white);
    letter-spacing: -4px;
  }
  .mubarak-word {
    position: absolute;
    left: 372px;
    top: 785px;
    margin: 0;
    font-family: "Montserrat", sans-serif;
    font-weight: 400;
    font-size: 36px;
    letter-spacing: 1px;
    color: var(--ink-soft);
  }
  .recipient-signature {
    position: absolute;
    left: 478px;
    top: 862px;
    margin: 0;
    font-family: "Allura", cursive;
    font-size: 46px;
    color: var(--ink-white);
    white-space: nowrap;
  }
  .recipient-signature .arabic-name {
    font-family: "Amiri", serif;
    font-size: 36px;
  }
</style>
</head>
<body>
  <main class="greeting-card">
    <div class="mosque-emblem" role="img" aria-label="White silhouette of a mosque with a dome, minaret and crescent finial"></div>
    <svg class="crescent-star" viewBox="0 0 115 125" aria-hidden="true">
      <path d="M58 4 A58 58 0 1 0 112 98 A48 48 0 1 1 58 4 Z" fill="var(--ink-white)"/>
      <polygon points="82,42 85.5,52 96,52 87.5,58 90.7,68 82,62 73.3,68 76.5,58 68,52 78.5,52" fill="var(--ink-white)"/>
    </svg>
    <h1 class="eid-title">Eid</h1>
    <p class="mubarak-word">MUBARAK</p>
    <p class="recipient-signature">-Oulima <span class="arabic-name">(أوليمة)</span></p>
  </main>
</body>
</html>
```